Hip and quirky Indian restaurant Menu

We need a build your own bowl/meal/wrap menu similar to Marwenda others. We would like illustrations if possible of India/veggies/chicken/animals/themes. Please utilize the colors that match the schema of the logos provided. We have included pictures you may use them if you would like to. Menu provided is our old menu.

Target Market(s)

Millenials, Ge

Industry/Entity Type

Retail

Font styles to use
Sans Serif
Decorative

Requirements
Must have
• logical placements for build your own meal options
Nice to have
• Illustrations.

```html
<!DOCTYPE html>
<html lang="en">
<head>
<meta charset="utf-8">
<title>Masala Lane – Menu</title>
<link href="https://fonts.googleapis.com/css2?family=Bebas+Neue&family=Montserrat:wght@500;700&display=swap" rel="stylesheet">
<style>
:root{
  --orange:#ee6640;
  --plum:#9c2262;
  --navy:#2e4389;
  --ink:#25245e;
  --red:#e8262f;
  --gold:#f9ae43;
  --cream:#fcdcaa;
  --paper:#fff8ee;
  --white:#ffffff;
}
*{margin:0;padding:0;box-sizing:border-box}
html,body{width:1200px;height:849px;overflow:hidden}
body{font-family:"Montserrat",sans-serif;background:var(--paper);position:relative}
.backdrop{position:absolute;inset:0;background:radial-gradient(circle at 50% 50%,var(--cream) 0%,#fde7c6 45%,var(--paper) 80%)}
.panel{position:absolute;background:var(--orange);color:var(--white)}
.display{font-family:"Bebas Neue",sans-serif;font-weight:400;letter-spacing:1px;line-height:.95}
.brand{left:12px;top:0;width:322px;height:284px;display:flex;flex-direction:column;align-items:center;justify-content:center;gap:10px}
.brand-mark{width:40px;height:40px;border-radius:50%;background:var(--white)}
.brand-name{font-family:"Montserrat",sans-serif;font-weight:700;font-size:30px;color:var(--white)}
.lassi{left:405px;top:0;width:340px;height:265px;padding:22px 28px 22px 29px}
.lassi h2{font-size:36px;text-align:center;margin-bottom:10px}
.price-table{width:100%;border-collapse:collapse;font-size:11.5px}
.price-table th{font-size:7px;font-weight:700;text-align:left;padding-bottom:6px}
.price-table td{padding:1.5px 0}
.price-table td:nth-child(2),.price-table th:nth-child(2){width:53px}
.price-table td:nth-child(3),.price-table th:nth-child(3){width:42px}
.photos{position:absolute;left:792px;top:15px;width:388px;height:360px;background:linear-gradient(135deg,#e9e4dc,#8a6a48 55%,#d9d3c9);border-radius:8px}
.build{position:absolute;left:0;top:298px;width:340px;text-align:center}
.build-title{font-size:56px}
.build-title .l1{color:var(--orange)}
.build-title .l2{color:var(--plum)}
.badge{display:inline-block;margin-top:8px;background:var(--orange);color:var(--white);font-size:18px;padding:3px 12px;border-radius:5px}
.step{position:absolute;left:12px;width:320px;text-align:center}
.step h3{font-size:14.5px;font-weight:700;margin-bottom:6px}
.band{padding:9px 20px;color:var(--white);font-size:11.2px;line-height:1.4;clip-path:polygon(2% 8%,100% 0,96% 30%,99% 70%,88% 100%,5% 96%,0 60%,3% 35%)}
.s1{top:452px}.s1 h3{color:var(--plum)}.s1 .band{background:var(--plum)}
.s2{top:553px}.s2 h3{color:var(--red)}.s2 .band{background:var(--red)}
.s3{top:654px}.s3 h3{color:var(--ink)}.s3 .band{background:var(--ink)}
.s4{top:752px}.s4 h3{color:var(--gold)}.s4 .band{background:var(--gold);padding:14px 20px}
.blob{position:absolute;color:var(--white);text-align:center;clip-path:polygon(4% 22%,30% 14%,42% 0,55% 20%,75% 18%,100% 24%,99% 72%,90% 90%,70% 86%,55% 100%,40% 88%,8% 92%,0 70%)}
.biryani{left:410px;top:290px;width:362px;height:265px;background:var(--navy);padding:72px 22px 0}
.biryani h2{font-size:34px;margin-bottom:10px}
.biryani p{font-size:11.3px;line-height:1.4}
.snacks{left:410px;top:560px;width:362px;height:250px;background:var(--plum);padding:60px 48px 0}
.snacks h2{font-size:34px;margin-bottom:4px}
.snack-list{list-style:none;font-size:11.5px;text-align:left}
.snack-list li{display:flex;justify-content:space-between;padding:1px 0}
.side{left:830px;top:388px;width:345px;height:461px;text-align:center;padding-top:50px}
.side h2{font-size:32px;line-height:.9;margin-bottom:10px}
.side ul{list-style:none;font-size:11.3px;line-height:15.3px}
.side .meals-list{margin-bottom:24px}
.side .fries-list{margin-bottom:16px}
.side .drinks-title{margin-bottom:8px}
</style>
</head>
<body>
<div class="backdrop" role="img" aria-label="Soft peach mandala pattern background"></div>

<header class="panel brand">
  <span class="brand-mark"></span>
  <span class="brand-name">Masala Lane</span>
</header>

<section class="panel lassi">
  <h2 class="display">Lassi/<br>Indian Shakes</h2>
  <table class="price-table">
    <tr><th></th><th>SMALL</th><th>LARGE</th></tr>
    <tr><td>Original Lassi</td><td>2.00</td><td>2.50</td></tr>
    <tr><td>Mango Lassi</td><td>2.5</td><td>3.00</td></tr>
    <tr><td>Rose Lassi</td><td>2.5</td><td>3.00</td></tr>
    <tr><td>Chai Spice Lassi</td><td>2.75</td><td>3.25</td></tr>
    <tr><td>Cookies N Cream Lassi</td><td>2.75</td><td>3.25</td></tr>
    <tr><td>Chocolate Hazelnut Lassi</td><td>2.75</td><td>3.25</td></tr>
  </table>
</section>

<div class="photos" role="img" aria-label="Photos of curry bowls, biryani and thali dishes on a wooden table"></div>

<section class="build">
  <h1 class="display build-title"><span class="l1">Build Your</span><br><span class="l2">Own Meal</span></h1>
  <span class="display badge">$8.00</span>
</section>

<div class="step s1"><h3>PICK BOWL/WRAP</h3><div class="band">Salad Bowl, Basmati Rice Bowl,<br>Curry Rice Bowl, Paratha Wrap</div></div>
<div class="step s2"><h3>PICK MAIN CURRY OPTION</h3><div class="band">Veg Korma, Chana Masala, CTM,<br>Chili Chicken, Tandoori Chicken,<br>Beef Curry +$1, Goat Curry $2</div></div>
<div class="step s3"><h3>PICK TOPPINGS</h3><div class="band">Beets Thoran, Green Beans Thoran,<br>Cabbage Thoran, Chick Pea Salad<br>Cucumber Salad, diced Onion</div></div>
<div class="step s4"><h3>PICK SAUCES</h3><div class="band">Original Mint, Sweet Tamarind,<br>Cool Yogurt, Mango Chilli, Tikka Masala</div></div>

<section class="blob biryani">
  <h2 class="display">Chicken<br>Biriyani Bowl</h2>
  <p>The Original Indian Rice Bowl! Chicken and rice which has been baked to perfection.” Served with yogurt sauce, pickle and pappadom.</p>
</section>

<section class="blob snacks">
  <h2 class="display">Snacks</h2>
  <ul class="snack-list">
    <li><span>Samosa</span><span>$1.00</span></li>
    <li><span>Veg Puffs</span><span>$1.49</span></li>
    <li><span>Egg Puffs</span><span>$2.49</span></li>
    <li><span>Sweet Puffs</span><span>$1.49</span></li>
    <li><span>Beef Puffs</span><span>$1.49</span></li>
    <li><span>Chicken Puffs</span><span>$1.49</span></li>
  </ul>
</section>

<section class="panel side">
  <h2 class="display">Chicken<br>Meals</h2>
  <ul class="meals-list"><li>Tandoori Chicken /Fries $7</li><li>Chicken Tender/ Fries $7</li><li>Spicy Chicken Tender/ Fries $7</li></ul>
  <h2 class="display">Loaded<br>Fries</h2>
  <ul class="fries-list"><li>Chicken Tikka Fries</li><li>Tandoori Fries</li><li>Chili Chicken Fries</li></ul>
  <h2 class="display drinks-title">Drinks</h2>
  <ul><li>Iced Tea 32oz</li><li>Lemonade 32oz</li><li>Masala Tea</li><li>Indian Coffee</li><li>Soda Can</li><li>Water Bottle</li></ul>
</section>
</body>
</html>
```